Industrial automation company needs new business cards

We need a new business card designed. We have an existing logo that is very simple and are happy to consider changes to it. We have been in business for more than 10 years and our logo has some brand recognition.
We are a company of engineers and build systems for industrial automation, substation automation, power and energy monitoring and production data vertical integration. Our main clients are food manufacturers, data centers and government establishments.
Our current business cards have our name, qualifications, job title, telephone, email and web address details. We don't need our physical address on our business cards. I've attached our current logo

Industry/Entity Type

Business

Logo Text

varlo

Font styles to use
Sans Serif

Colors
6b449b

Requirements
Must have
• - double sided business cards
• - name (eg Hello There)
• - qualifications (BE Elec MIRQT)
• - job title (eg Senior Engineer)
• - telephone (eg 0400 000 000)
• - email (eg hello.there@varlo.com.au)
• - web address (eg varlo.com.au)
Nice to have
• include our target markets on the back side of the card
• - industrial automation
• - substation automation
• - power and energy monitoring
• - production data vertical integration

```html
<!DOCTYPE html>
<html lang="en">
<head>
<meta charset="utf-8">
<title>Varlo – Business Card Design</title>
<link rel="stylesheet" href="https://fonts.googleapis.com/css2?family=Oswald:wght@300;400;600&family=Montserrat:wght@500&display=swap">
<style>
  :root {
    --bg: #efefef;
    --violet-1: #9a6be0;
    --violet-2: #7b56b3;
    --violet-3: #6b449b;
    --violet-4: #553581;
    --violet-5: #43296b;
    --lilac: #b89ae0;
    --mauve: #8f79ad;
    --white: #ffffff;
    --shadow: rgba(0,0,0,0.35);
  }
  html, body {
    margin: 0;
    padding: 0;
    overflow: hidden;
  }
  body {
    width: 1200px;
    height: 1000px;
    background: radial-gradient(circle at 50% 45%, #fafafa 0%, var(--bg) 70%, #e2e2e2 100%);
    position: relative;
    font-family: "Oswald", sans-serif;
  }
  .brand-mark {
    position: absolute;
    left: 50px;
    top: 70px;
    width: 350px;
    height: 310px;
    display: flex;
    align-items: center;
    justify-content: center;
    gap: 16px;
  }
  .brand-mark__dot {
    width: 30px;
    height: 30px;
    border-radius: 50%;
    background: var(--violet-3);
  }
  .brand-mark__name {
    font-family: "Oswald", sans-serif;
    font-weight: 600;
    font-size: 72px;
    letter-spacing: 4px;
    color: var(--violet-3);
    text-transform: uppercase;
  }
  .palette__swatch {
    position: absolute;
    box-shadow: 6px 6px 8px var(--shadow);
  }
  .swatch-1 { left: 148px; top: 469px; width: 148px; height: 141px; background: var(--violet-1); }
  .swatch-2 { left: 148px; top: 616px; width: 148px; height: 72px;  background: var(--violet-2); }
  .swatch-3 { left: 148px; top: 694px; width: 148px; height: 62px;  background: var(--violet-3); }
  .swatch-4 { left: 148px; top: 762px; width: 148px; height: 60px;  background: var(--violet-4); }
  .swatch-5 { left: 143px; top: 834px; width: 158px; height: 101px; background: var(--violet-5); }

  .card {
    position: absolute;
    left: 499px;
    width: 611px;
    height: 396px;
    overflow: hidden;
    box-shadow: 6px 6px 8px var(--shadow);
  }
  .card svg { position: absolute; inset: 0; }
  .card--front { top: 72px; }
  .card--back { top: 534px; }

  .front__identity {
    position: absolute;
    right: 46px;
    top: 82px;
    text-align: right;
    color: var(--white);
    text-transform: uppercase;
  }
  .front__name {
    font-weight: 600;
    font-size: 54px;
    line-height: 1;
    text-shadow: 2px 3px 4px rgba(0,0,0,0.45);
  }
  .front__title {
    font-weight: 300;
    font-size: 35px;
    line-height: 1.4;
  }
  .front__quals {
    font-weight: 300;
    font-size: 20px;
    letter-spacing: 1px;
    line-height: 1.2;
  }
  .front__contacts {
    position: absolute;
    left: 0;
    top: 235px;
    margin: 0;
    padding: 0;
    list-style: none;
  }
  .contact {
    display: flex;
    align-items: center;
    height: 43px;
    margin-bottom: 5px;
    color: var(--white);
    font-family: "Montserrat", sans-serif;
    font-weight: 500;
    font-size: 15px;
    text-transform: uppercase;
  }
  .contact__icon {
    width: 55px;
    height: 41px;
    border: 1px solid var(--white);
    border-left: none;
    box-sizing: border-box;
    display: flex;
    align-items: center;
    justify-content: center;
    margin-right: 10px;
  }

  .back__label {
    position: absolute;
    color: var(--white);
    font-weight: 300;
    font-size: 18px;
    line-height: 1.05;
    text-align: center;
    white-space: nowrap;
    transform: translate(-50%, -50%) rotate(var(--angle));
  }
  .label-tl { left: 62px;  top: 62px;  --angle: -45deg; }
  .label-tr { left: 549px; top: 62px;  --angle: 45deg; }
  .label-bl { left: 62px;  top: 334px; --angle: 45deg; }
  .label-br { left: 549px; top: 334px; --angle: -45deg; }

  .back__brand {
    position: absolute;
    left: 0;
    right: 0;
    top: 150px;
    display: flex;
    align-items: center;
    justify-content: center;
    gap: 14px;
  }
  .back__brand .brand-mark__name { font-size: 64px; color: var(--violet-5); }
  .back__brand .brand-mark__dot { background: var(--violet-5); width: 26px; height: 26px; }
</style>
</head>
<body>

  <div class="brand-mark">
    <span class="brand-mark__dot"></span>
    <span class="brand-mark__name">varlo</span>
  </div>

  <div class="palette" aria-label="Colour palette">
    <div class="palette__swatch swatch-1"></div>
    <div class="palette__swatch swatch-2"></div>
    <div class="palette__swatch swatch-3"></div>
    <div class="palette__swatch swatch-4"></div>
    <div class="palette__swatch swatch-5"></div>
  </div>

  <section class="card card--front">
    <svg width="611" height="396" viewBox="0 0 611 396">
      <defs>
        <radialGradient id="front-glow" cx="0.62" cy="0.38" r="0.6">
          <stop offset="0" stop-color="#8b62d0"/>
          <stop offset="1" stop-color="#4a2d77"/>
        </radialGradient>
      </defs>
      <rect width="611" height="396" fill="url(#front-glow)"/>
      <polygon points="0,0 171,0 409,396 0,396" fill="var(--violet-3)"/>
      <polygon points="0,0 120,0 340,396 220,396" fill="var(--violet-5)"/>
      <polygon points="0,120 0,260 225,396 120,396" fill="var(--violet-2)" opacity="0.6"/>
      <polygon points="60,0 171,0 260,150" fill="var(--violet-2)" opacity="0.5"/>
      <line x1="171" y1="0" x2="409" y2="396" stroke="var(--white)" stroke-width="2"/>
    </svg>

    <div class="front__identity">
      <div class="front__name">Hello There</div>
      <div class="front__title">Senior Engineer</div>
      <div class="front__quals">(BE Elec., MIRQT)</div>
    </div>

    <ul class="front__contacts">
      <li class="contact">
        <span class="contact__icon">
          <svg width="26" height="18" viewBox="0 0 26 18" style="position:static"><rect width="26" height="18" fill="#fff"/><polyline points="0,0 13,10 26,0" fill="none" stroke="#6b449b" stroke-width="1.5"/></svg>
        </span>
        hello.there@varlo.com.au
      </li>
      <li class="contact">
        <span class="contact__icon">
          <svg width="26" height="24" viewBox="0 0 26 24" style="position:static"><polygon points="13,1 26,13 22,13 22,24 16,24 16,16 10,16 10,24 4,24 4,13 0,13" fill="#fff"/></svg>
        </span>
        varlo.com.au
      </li>
      <li class="contact">
        <span class="contact__icon">
          <svg width="24" height="24" viewBox="0 0 24 24" style="position:static"><path d="M5 2 L9 7 L7 10 Q10 15 14 17 L17 15 L22 19 L19 23 Q10 22 3 12 Q1 6 5 2 Z" fill="#fff"/></svg>
        </span>
        0400 000 000
      </li>
    </ul>
  </section>

  <section class="card card--back">
    <svg width="611" height="396" viewBox="0 0 611 396">
      <rect width="611" height="396" fill="var(--lilac)"/>
      <polygon points="0,0 250,0 470,396 0,396" fill="var(--mauve)" opacity="0.75"/>
      <polygon points="380,0 611,0 611,230" fill="#c6abe8" opacity="0.8"/>
      <polygon points="0,180 300,396 0,396" fill="#a68ac8" opacity="0.7"/>
      <polygon points="180,396 420,120 611,300 611,396" fill="#8a74a8" opacity="0.5"/>
      <polygon points="0,0 156,0 0,156" fill="var(--violet-3)"/>
      <polygon points="456,0 611,0 611,156" fill="var(--violet-3)"/>
      <polygon points="0,241 0,396 156,396" fill="var(--violet-3)"/>
      <polygon points="611,241 611,396 456,396" fill="var(--violet-3)"/>
    </svg>

    <div class="back__label label-tl">Industrial<br>Automation</div>
    <div class="back__label label-tr">Substation<br>Automation</div>
    <div class="back__label label-bl">Production Data<br>Vertical Integration</div>
    <div class="back__label label-br">Power &amp; Energy<br>Monitoring</div>

    <div class="back__brand">
      <span class="brand-mark__dot"></span>
      <span class="brand-mark__name">varlo</span>
    </div>
  </section>

</body>
</html>
```